Business Card Design Project

Our organization is in need of a business card design with the use of our logo. We are looking for professional design that will embellish the image our consulting firm.

Here is a summary of what we do: Quorvent is systems consulting firm that specializes in the management, migration, and maintenance of IT infrastructure solutions.

Here is a link to my website: http://quorvent-example.com

I have attached the logo.

Target Market(s)

Organization that need IT and server support.

Industry/Entity Type

Business

```html
<!DOCTYPE html>
<html lang="en">
<head>
<meta charset="utf-8">
<title>Quorvent — Business Card</title>
<link href="https://fonts.googleapis.com/css2?family=Questrial&display=swap" rel="stylesheet">
<style>
  :root {
    --navy: #2b3556;
    --orange: #f07a2c;
    --ink: #3a3a3a;
    --paper: #ffffff;
    --band: #ededed;
    --backdrop: #e4e7ea;
  }
  * { box-sizing: border-box; margin: 0; padding: 0; }
  html, body {
    width: 1200px; height: 960px; overflow: hidden;
    background: var(--backdrop);
    font-family: "Questrial", "Century Gothic", sans-serif;
    color: var(--ink);
  }
  .sheet {
    position: relative; width: 1200px; height: 960px;
    display: flex; flex-direction: column; align-items: center; justify-content: center; gap: 60px;
  }
  .card {
    position: relative; width: 700px; height: 400px;
    background: var(--paper);
    box-shadow: 0 4px 18px rgba(0,0,0,.12);
    overflow: hidden;
  }
  .card-bands { position: absolute; inset: 0; }

  /* Front */
  .front-brand {
    position: absolute; left: 60px; top: 0; height: 400px;
    display: flex; align-items: center; gap: 14px;
  }
  .brand-dot { width: 30px; height: 30px; border-radius: 50%; background: var(--navy); }
  .brand-name { font-size: 44px; color: var(--navy); letter-spacing: .5px; }

  .front-details { position: absolute; left: 420px; top: 70px; width: 250px; }
  .person-name { font-size: 30px; letter-spacing: .5px; color: var(--ink); }
  .person-role { font-size: 19px; margin-top: 4px; }
  .rule { height: 2px; background: var(--orange); margin: 16px 0 16px -10px; }
  .contact { list-style: none; font-size: 19px; }
  .contact li { display: flex; align-items: center; gap: 10px; height: 25px; }
  .contact svg { width: 15px; height: 15px; flex: none; }
  .address { font-size: 19px; line-height: 26px; padding-left: 10px; }

  /* Back */
  .back-brand {
    position: absolute; left: 70px; top: 110px;
    display: flex; align-items: center; gap: 18px;
  }
  .back-brand .brand-name { font-size: 64px; }
  .divider { width: 3px; height: 120px; background: var(--orange); margin: 0 22px; }
  .tagline {
    position: absolute; left: 0; right: 0; top: 300px; text-align: center;
    padding-left: 120px;
    color: var(--orange); font-size: 20px; letter-spacing: 3px;
  }
</style>
</head>
<body>
<main class="sheet">

  <section class="card card-front" aria-label="Card front">
    <svg class="card-bands" viewBox="0 0 700 400" preserveAspectRatio="none" aria-hidden="true">
      <polygon points="0,330 700,80 700,200 0,400" fill="var(--band)"/>
      <polygon points="0,400 700,200 700,260 120,400" fill="#f4f4f4"/>
    </svg>

    <div class="front-brand">
      <span class="brand-dot"></span>
      <span class="brand-name">Quorvent</span>
    </div>

    <div class="front-details">
      <h1 class="person-name">JOHN DOE</h1>
      <p class="person-role">Managing Partner</p>
      <div class="rule"></div>
      <ul class="contact">
        <li>
          <svg viewBox="0 0 16 16" aria-hidden="true"><rect x="3" y="1" width="10" height="14" rx="2" fill="var(--orange)"/><rect x="5" y="3" width="6" height="8" fill="#fff"/></svg>
          210.555.0143
        </li>
        <li>
          <svg viewBox="0 0 16 16" aria-hidden="true"><rect x="4" y="1" width="8" height="5" fill="var(--orange)"/><rect x="1" y="6" width="14" height="6" rx="1" fill="var(--orange)"/><rect x="4" y="10" width="8" height="5" fill="#fff" stroke="var(--orange)" stroke-width="1.5"/></svg>
          210.555.0144
        </li>
        <li>
          <svg viewBox="0 0 16 16" aria-hidden="true"><circle cx="8" cy="8" r="7" fill="var(--orange)"/><path d="M1 8h14M8 1c-3 3-3 11 0 14M8 1c3 3 3 11 0 14" stroke="#fff" stroke-width="1.2" fill="none"/></svg>
          quorvent-example.com
        </li>
      </ul>
      <div class="rule"></div>
      <p class="address">1842 Ridgeway Dr<br>Cedar Falls, TX 78012</p>
    </div>
  </section>

  <section class="card card-back" aria-label="Card back">
    <div class="back-brand">
      <span class="brand-dot"></span>
      <span class="divider"></span>
      <span class="brand-name">quorvent</span>
    </div>
    <p class="tagline">SYSTEM SOLUTIONS</p>
  </section>

</main>
</body>
</html>
```